New professional looking flyer for company

I need our flyer updated my flyer is the Lvb flyer Have attached current flyer so you know what services need to be listed. Want it to be in mainly dark colours like black and dark grey with pops of light grey, silver or white. i have added several photos for you to choose which ones work best with your design would like The photos to be in colour for the flyer. But can have a mix of greyscale if that works for your design j have attached another companies flyers as design ideas to show what I am looking for

Target Market(s)

new clients

Industry/Entity Type

transport and earthmoving

Colors

Designer to choose colors to be used in the design.

Requirements
Nice to have
• Look professional
Should not have
• No orange or red or green

```html
<!DOCTYPE html>
<html lang="en">
<head>
<meta charset="utf-8">
<title>Mesa Vale Services Flyer</title>
<link rel="stylesheet" href="https://fonts.googleapis.com/css2?family=Exo+2:ital,wght@0,400;0,500;0,600;0,700;0,800;1,700&display=swap">
<style>
:root{
  --stage:#232323;
  --ink-dark:#1d1d1d;
  --panel:rgba(40,40,40,.82);
  --gold:#d9a21b;
  --gold-deep:#b07d0c;
  --white:#ffffff;
  --silver:#cfcfcf;
  --text-light:#f2f2f2;
  --text-dark:#222;
}
*{margin:0;padding:0;box-sizing:border-box}
html,body{width:669px;height:1200px;overflow:hidden;background:var(--stage)}
body{font-family:"Exo 2",sans-serif;position:relative}
.flyer{position:absolute;left:24.5px;top:199px;width:749px;height:969px;transform:scale(.828);transform-origin:0 0;background:var(--ink-dark);overflow:hidden}
.bg-photo{position:absolute;left:0;top:0;width:347px;height:492px;background:linear-gradient(180deg,#8ea4b4 0%,#6f6a5e 45%,#4b3e30 100%)}
.title-panel{position:absolute;left:27px;top:0;width:320px;height:492px;background:var(--panel)}
.hero-photo{position:absolute;left:347px;top:0;width:402px;height:420px;background:linear-gradient(180deg,#9cc3dc 0%,#b8c9cf 30%,#a9a9a6 60%,#6e665c 100%)}
.gold-rule{position:absolute;left:0;top:490px;width:749px;height:5px;background:var(--gold)}
.thumb{position:absolute;top:424px;width:165px;height:121px;border:2px solid var(--white)}
.thumb-a{left:360px;background:linear-gradient(180deg,#7fa6cc 0%,#b6c3c9 45%,#8a5a45 100%)}
.thumb-b{left:537px;background:linear-gradient(180deg,#3f7fc4 0%,#8fb0cb 40%,#c48f55 100%)}
.brand{position:absolute;left:64px;top:42px;width:214px;text-align:center;color:var(--silver)}
.brand-rule{height:2px;background:#9a9a9a}
.brand-name{font-size:62px;font-weight:800;letter-spacing:4px;line-height:1;margin:8px 0 4px}
.brand-sub{font-size:20px;font-weight:500;margin-bottom:6px}
.headline{position:absolute;left:56px;top:192px;color:var(--white);font-weight:800;line-height:.9}
.headline .line{display:block;font-size:104px;letter-spacing:-1px}
.headline .tag{display:block;font-size:56px;color:var(--gold);margin-top:14px;letter-spacing:1px}
.services-title{position:absolute;left:25px;top:505px;font-size:44px;font-weight:700;color:var(--silver)}
.service-list{position:absolute;list-style:none;color:var(--text-light);font-size:22px;font-weight:500}
.service-list li{display:flex;align-items:flex-start;height:37.3px}
.service-list svg{width:20px;height:20px;margin:3px 11px 0 0;flex:none}
.list-left{left:27px;top:563px}
.list-right{left:444px;top:563px}
.list-right li.two-line{height:auto;line-height:1.2}
.cta-band{position:absolute;left:0;top:801px;width:749px;height:87px;background:var(--white)}
.cta-copy{position:absolute;left:27px;top:810px;color:var(--text-dark)}
.cta-copy .small{font-size:16px;font-weight:400}
.cta-copy .strong{font-size:21px;font-weight:700;color:var(--gold-deep);line-height:1.25}
.truck-photo{position:absolute;left:446px;top:765px;width:300px;height:140px;background:linear-gradient(180deg,#ffffff 0%,#bdb3a4 40%,#3a3a3a 100%);border-radius:2px}
.phone-band{position:absolute;left:0;top:903px;width:400px;height:66px}
.phone{position:absolute;left:27px;top:912px;display:flex;align-items:center;gap:18px;font-size:44px;font-weight:800;color:var(--ink-dark)}
.phone svg{width:34px;height:34px}
.contact{position:absolute;left:403px;top:912px;font-size:14px;font-weight:500;color:var(--text-light);line-height:1.7}
.contact div{display:flex;align-items:center;gap:8px}
.contact svg{width:11px;height:11px}
</style>
</head>
<body>
<main class="flyer">
  <div class="bg-photo" role="img" aria-label="Photo of a road train with trailers parked on red outback ground"></div>
  <div class="title-panel"></div>
  <div class="hero-photo" role="img" aria-label="Photo of a white prime mover with an oversize sign under a blue sky"></div>
  <div class="gold-rule"></div>
  <div class="thumb thumb-a" role="img" aria-label="Photo of road trains on an outback yard"></div>
  <div class="thumb thumb-b" role="img" aria-label="Photo of a loader carried on a truck trailer"></div>

  <div class="brand">
    <div class="brand-rule"></div>
    <div class="brand-name">LVB</div>
    <div class="brand-sub">Pty Ltd</div>
    <div class="brand-rule"></div>
  </div>

  <h1 class="headline">
    <span class="line">MESA</span>
    <span class="line">VALE</span>
    <span class="tag">SERVICES</span>
  </h1>

  <h2 class="services-title">Our Services</h2>
  <ul class="service-list list-left">
    <li><svg viewBox="0 0 20 20"><circle cx="10" cy="10" r="8.5" fill="none" stroke="#d9a21b" stroke-width="1.6"/><path d="M6 10.5l3 3 5.5-6.5" fill="none" stroke="#d9a21b" stroke-width="1.8"/></svg>Over size loads / Hot Shot Loads</li>
    <li><svg viewBox="0 0 20 20"><circle cx="10" cy="10" r="8.5" fill="none" stroke="#d9a21b" stroke-width="1.6"/><path d="M6 10.5l3 3 5.5-6.5" fill="none" stroke="#d9a21b" stroke-width="1.8"/></svg>Heavy Vehicle Recovery Services</li>
    <li><svg viewBox="0 0 20 20"><circle cx="10" cy="10" r="8.5" fill="none" stroke="#d9a21b" stroke-width="1.6"/><path d="M6 10.5l3 3 5.5-6.5" fill="none" stroke="#d9a21b" stroke-width="1.8"/></svg>Potable Water Deliveries</li>
    <li><svg viewBox="0 0 20 20"><circle cx="10" cy="10" r="8.5" fill="none" stroke="#d9a21b" stroke-width="1.6"/><path d="M6 10.5l3 3 5.5-6.5" fill="none" stroke="#d9a21b" stroke-width="1.8"/></svg>Road Building / Maintenance</li>
    <li><svg viewBox="0 0 20 20"><circle cx="10" cy="10" r="8.5" fill="none" stroke="#d9a21b" stroke-width="1.6"/><path d="M6 10.5l3 3 5.5-6.5" fill="none" stroke="#d9a21b" stroke-width="1.8"/></svg>Earthworks</li>
    <li><svg viewBox="0 0 20 20"><circle cx="10" cy="10" r="8.5" fill="none" stroke="#d9a21b" stroke-width="1.6"/><path d="M6 10.5l3 3 5.5-6.5" fill="none" stroke="#d9a21b" stroke-width="1.8"/></svg>Sand &amp; Metal Supply &amp; Cartage</li>
  </ul>
  <ul class="service-list list-right">
    <li><svg viewBox="0 0 20 20"><circle cx="10" cy="10" r="8.5" fill="none" stroke="#d9a21b" stroke-width="1.6"/><path d="M6 10.5l3 3 5.5-6.5" fill="none" stroke="#d9a21b" stroke-width="1.8"/></svg>Road Train Tippers</li>
    <li><svg viewBox="0 0 20 20"><circle cx="10" cy="10" r="8.5" fill="none" stroke="#d9a21b" stroke-width="1.6"/><path d="M6 10.5l3 3 5.5-6.5" fill="none" stroke="#d9a21b" stroke-width="1.8"/></svg>Road Train Tankers</li>
    <li><svg viewBox="0 0 20 20"><circle cx="10" cy="10" r="8.5" fill="none" stroke="#d9a21b" stroke-width="1.6"/><path d="M6 10.5l3 3 5.5-6.5" fill="none" stroke="#d9a21b" stroke-width="1.8"/></svg>Road Train Flat Tops</li>
    <li><svg viewBox="0 0 20 20"><circle cx="10" cy="10" r="8.5" fill="none" stroke="#d9a21b" stroke-width="1.6"/><path d="M6 10.5l3 3 5.5-6.5" fill="none" stroke="#d9a21b" stroke-width="1.8"/></svg>Drop Deck Trailers</li>
    <li class="two-line"><svg viewBox="0 0 20 20"><circle cx="10" cy="10" r="8.5" fill="none" stroke="#d9a21b" stroke-width="1.6"/><path d="M6 10.5l3 3 5.5-6.5" fill="none" stroke="#d9a21b" stroke-width="1.8"/></svg><span>Mine Site accredited<br>equipment &amp; Operators</span></li>
  </ul>

  <div class="cta-band"></div>
  <div class="cta-copy">
    <p class="small">We offer a large range of services not listed so</p>
    <p class="strong">Call us today for a personalised<br>quote to suit your needs.</p>
  </div>
  <div class="truck-photo" role="img" aria-label="Photo of a dark prime mover hauling site buildings as an oversize road train"></div>

  <svg class="phone-band" viewBox="0 0 400 66" preserveAspectRatio="none"><polygon points="0,0 400,0 366,66 0,66" fill="#d9a21b"/></svg>
  <div class="phone">
    <svg viewBox="0 0 34 34"><circle cx="17" cy="17" r="15" fill="none" stroke="#1d1d1d" stroke-width="3"/><path d="M11 9c1-1 2-1 3 0l2 3c.5 1 0 2-1 2.5 1 2 2.5 3.5 4.5 4.5.5-1 1.5-1.5 2.5-1l3 2c1 1 1 2 0 3-2 2-5 2-9-1.5S9 12 11 9z" fill="#1d1d1d"/></svg>
    <span>040 555 0199</span>
  </div>
  <div class="contact">
    <div><svg viewBox="0 0 12 12"><path d="M6 0a4 4 0 0 1 4 4c0 3-4 8-4 8S2 7 2 4a4 4 0 0 1 4-4z" fill="#d9a21b"/><circle cx="6" cy="4" r="1.5" fill="#1d1d1d"/></svg>Depot: Lot 41, Saltbush Track Road Dunmore</div>
    <div><svg viewBox="0 0 12 12"><rect x="0" y="2" width="12" height="8" fill="#d9a21b"/><path d="M0 2l6 4 6-4" fill="none" stroke="#1d1d1d" stroke-width="1"/></svg>info@mesavaleservices.com.au</div>
  </div>
</main>
</body>
</html>
```